Tarvenna Shield / Melbrook Trophy / American football

We are looking for someone who can design our flyers for the above for a Sports Bar & Grill Grill in the Caribbean.
Once we see drafts we can give the designer the specials for our events to be added. The above in title are just example of what we will be advised, not all topics on one ad as some designers have already provided, apologies for not clarification in tittle.
I am attaching our logo and map location of that can be used.
If we pick a person we will continue to use them for all our advert flyers and possibly more marketing items.
Thanks in advance for submitting.

Target Market(s)

New, current customers and tourists

Industry/Entity Type

Food and beverage

Requirements
Must have
• Logo, info on event and or events

```html
<!DOCTYPE html>
<html lang="en">
<head>
<meta charset="utf-8">
<title>Melbrook Trophy – Game Time Specials</title>
<link rel="stylesheet" href="https://fonts.googleapis.com/css2?family=Teko:wght@500;600;700&family=Montserrat:wght@500;700;800&display=swap">
<style>
  :root {
    --page-bg: #d9d9d9;
    --sky-top: #3a0e08;
    --sky-mid: #b8410f;
    --sky-glow: #f08a2a;
    --stadium: #2b2a30;
    --field-light: #3f6a2a;
    --field-dark: #1b2e14;
    --gold-light: #ffe066;
    --gold-deep: #f09a0c;
    --silver-light: #ffffff;
    --silver-mid: #c9c9c9;
    --silver-dark: #8a8a8a;
    --white: #ffffff;
    --badge: #f4b01a;
    --ink: #1a1a1a;
    --brand: #f3a23a;
    --map: #9a7b5a;
  }
  * { box-sizing: border-box; margin: 0; padding: 0; }
  html, body { width: 1200px; height: 2353px; overflow: hidden; }
  body { background: var(--page-bg); position: relative; font-family: "Montserrat", sans-serif; }

  .flyer {
    position: absolute; left: 50px; top: 464px;
    width: 1100px; height: 1424px; overflow: hidden;
    box-shadow: 0 20px 40px rgba(0,0,0,.35);
  }
  .scene-photo {
    position: absolute; inset: 0;
    background:
      radial-gradient(ellipse 70% 14% at 55% 36%, rgba(255,255,255,.35), transparent 70%),
      linear-gradient(180deg, var(--sky-top) 0%, var(--sky-mid) 18%, var(--sky-glow) 30%, #8a3a18 38%, var(--stadium) 44%, #3a3a40 48%, var(--field-light) 52%, #2c4c1e 70%, var(--field-dark) 100%);
  }
  .abs { position: absolute; white-space: nowrap; }

  .brand { left: 48px; top: 60px; width: 330px; text-align: center; }
  .brand-mark { width: 150px; height: 150px; border-radius: 50%; background: var(--white); margin: 0 auto 14px; }
  .brand-name { font-family: "Teko", sans-serif; font-weight: 700; color: var(--brand); font-size: 78px; line-height: .9; }
  .brand-sub { font-family: "Teko", sans-serif; font-weight: 700; color: var(--brand); font-size: 34px; line-height: 1; }

  .gold, .silver { -webkit-background-clip: text; background-clip: text; color: transparent; }
  .gold { background-image: linear-gradient(180deg, var(--gold-light) 0%, var(--gold-deep) 100%); }
  .silver { background-image: linear-gradient(180deg, var(--silver-light) 0%, var(--silver-mid) 50%, var(--silver-dark) 60%, var(--silver-light) 100%); }

  .display { font-family: "Teko", sans-serif; font-weight: 700; text-transform: uppercase; line-height: .85; filter: drop-shadow(3px 4px 3px rgba(0,0,0,.55)); }

  .event-name { left: 405px; top: 48px; width: 650px; text-align: center; font-size: 84px; }
  .event-title { left: 405px; top: 142px; width: 650px; text-align: center; font-size: 150px; line-height: .92; }

  .hero-art {
    left: 40px; top: 430px; width: 520px; height: 795px;
    background: radial-gradient(ellipse 45% 50% at 40% 45%, rgba(246,170,40,.85), rgba(200,110,20,.45) 55%, transparent 80%);
  }

  .specials-head { left: 589px; top: 705px; font-size: 108px; }
  .specials-sub { left: 589px; top: 800px; font-size: 108px; }

  .pint-dollar { left: 586px; top: 912px; font-size: 66px; }
  .pint-price { left: 614px; top: 905px; font-size: 150px; }
  .pint-info { left: 700px; top: 908px; color: var(--white); }
  .pint-info .label { font-family: "Montserrat", sans-serif; font-weight: 800; font-size: 44px; line-height: 1; }
  .pint-info .note { font-size: 18px; font-weight: 500; line-height: 1.2; }
  .pint-info .brandline { font-size: 17px; font-weight: 800; color: var(--gold-deep); line-height: 1.05; }

  .divider-v { left: 876px; top: 912px; width: 2px; height: 126px; background: var(--white); opacity: .8; }
  .drink-list { left: 890px; top: 912px; list-style: none; color: var(--white); }
  .drink-list li { font-size: 16px; font-weight: 800; line-height: 1.1; margin-bottom: 4px; }
  .price-badge { display: inline-block; background: var(--badge); color: var(--ink); font-size: 14px; padding: 0 4px; margin-top: 2px; }

  .divider-h { left: 589px; top: 1052px; width: 464px; height: 2px; background: var(--white); opacity: .85; }

  .date-day { left: 586px; top: 1074px; font-size: 100px; }
  .date-month { left: 790px; top: 1070px; font-family: "Montserrat", sans-serif; font-weight: 800; font-size: 48px; color: var(--white); line-height: 1; }
  .date-weekday { left: 798px; top: 1122px; font-family: "Montserrat", sans-serif; font-weight: 800; font-size: 46px; line-height: 1; }

  .location-map {
    left: 625px; top: 1186px; width: 475px; height: 200px;
    background: radial-gradient(ellipse 60% 45% at 55% 50%, var(--map), rgba(154,123,90,.4) 70%, transparent 90%);
  }

  .tagline { left: 50px; top: 1248px; color: var(--white); font-weight: 700; font-size: 31px; }
  .slogan { left: 50px; top: 1283px; font-weight: 800; font-size: 58px; line-height: 1.05; filter: drop-shadow(2px 3px 2px rgba(0,0,0,.5)); }
  .web { left: 52px; top: 1352px; color: var(--white); font-weight: 700; font-size: 21px; letter-spacing: 9px; }
</style>
</head>
<body>
  <main class="flyer">
    <div class="scene-photo" role="img" aria-label="Stadium at sunset with floodlights over a green field"></div>

    <div class="abs brand">
      <div class="brand-mark"></div>
      <div class="brand-name">Brennick's</div>
      <div class="brand-sub">Sports Bar &amp; Grill</div>
    </div>

    <h2 class="abs display gold event-name">Tarvenna Shield</h2>
    <h1 class="abs display silver event-title">Melbrook<br>Trophy</h1>

    <div class="abs hero-art" role="img" aria-label="Splashing pint of beer with a football helmet and ball"></div>

    <div class="abs display gold specials-head">Game Time</div>
    <div class="abs display silver specials-sub">Specials</div>

    <div class="abs display gold pint-dollar">$</div>
    <div class="abs display gold pint-price">5</div>
    <div class="abs pint-info">
      <div class="label">PINTS</div>
      <div class="note">Includes</div>
      <div class="brandline">ALL HARBORLINE<br>PRODUCTS</div>
    </div>

    <div class="abs divider-v"></div>
    <ul class="abs drink-list">
      <li>HERBAL BOMB<br><span class="price-badge">$4.50</span></li>
      <li>VODKA COCKTAILS<br><span class="price-badge">$4.50</span></li>
      <li>DEER &amp; A BEER<br><span class="price-badge">$4.50</span></li>
    </ul>

    <div class="abs divider-h"></div>
    <div class="abs display silver date-day">20TH</div>
    <div class="abs date-month">OCTOBER</div>
    <div class="abs gold date-weekday">FRIDAY</div>

    <div class="abs location-map" role="img" aria-label="Island map marking the bar's location"></div>

    <p class="abs tagline">NO GIMMICKS NO NONSENSE</p>
    <p class="abs gold slogan">WE ARE SPORTS</p>
    <p class="abs web">www.brennickssports.com</p>
  </main>
</body>
</html>
```